We need a full website with logo/graphics/woocommerce for hemp-based company

This site will be lunavetta.com. It is a website featuring the fact we are the only manufacturer to produce CBDP and THCP. It should be great on mobile and desktop. We will pay for any extensions needed and while it should be a simple site:

About Us
About the Laboratory
About CBDP
About THCP
Shop
Contact Us

Only 4 products on the site.

It can be wordpress or joomla. Your choice. You must install the final website on our server. We agree to pay for monthly support that must be submitted in your quote.

He have a great graphics designer that will assist keeping colors and graphics clean according to your specifications.

Industry/Entity Type

Hemp CBD THC

Coding

Coded - Design and coding required

Number of Pages Required

5+ page

Requirements
Must have
• A simple clean layout

```html
<!DOCTYPE html>
<html lang="en">
<head>
<meta charset="utf-8">
<title>Lunavetta</title>
<link href="https://fonts.googleapis.com/css2?family=Nunito:wght@700;800;900&family=Open+Sans:wght@400;600&family=Arimo:wght@400;700&display=swap" rel="stylesheet">
<style>
:root{
  --green:#12a150;
  --green-deep:#0b8a45;
  --green-bright:#07e36e;
  --mint:#e3f2e2;
  --mint-soft:#f2faf1;
  --ink:#444444;
  --text:#555555;
  --footer:#333333;
  --white:#ffffff;
}
*{margin:0;padding:0;box-sizing:border-box}
html,body{width:1200px;height:2768px;overflow:hidden;background:var(--white)}
body{font-family:"Open Sans",sans-serif;color:var(--text)}
.page{position:relative;width:1200px;height:2768px;overflow:hidden}
.abs{position:absolute}
.brand{display:flex;align-items:center;gap:8px;font-family:"Nunito",sans-serif;font-weight:800;color:var(--green);white-space:nowrap}
.brand-dot{border-radius:50%;background:var(--green)}
.nav{position:absolute;left:0;top:0;width:1200px;height:54px;border-bottom:1px solid #eee;background:var(--white);z-index:5}
.nav .brand{position:absolute;left:193px;top:12px;font-size:19px}
.nav .brand-dot{width:30px;height:30px}
.nav-link{position:absolute;top:22px;font-size:9.5px;line-height:12px;color:var(--ink);white-space:nowrap}
.nav-icons{position:absolute;left:927px;top:12px;width:44px;height:32px;display:flex;align-items:center;justify-content:center;border-left:1px solid #ddd;border-right:1px solid #ddd}
.nav-search{position:absolute;left:982px;top:19px}
.btn{position:absolute;display:flex;align-items:center;justify-content:center;gap:10px;height:39px;width:144px;border-radius:3px;background:linear-gradient(90deg,var(--green),var(--green-bright));color:var(--white);font-family:"Nunito",sans-serif;font-weight:800;font-size:14px;letter-spacing:.3px;white-space:nowrap;box-shadow:0 6px 14px rgba(7,160,80,.25)}
.hero-title{left:193px;top:168px;font-family:"Nunito",sans-serif;font-weight:900;font-size:70px;color:var(--green);line-height:1;white-space:nowrap}
.hero-sub{left:195px;top:241px;font-size:20px;color:var(--ink);white-space:nowrap}
.hero-text{left:195px;top:276px;font-size:12px;line-height:17px;color:#333;width:320px}
.art{position:absolute;border-radius:40px}
.eyebrow{font-family:"Nunito",sans-serif;font-weight:900;font-size:19px;letter-spacing:4.5px;color:var(--green);white-space:nowrap}
.heading{font-family:"Nunito",sans-serif;font-weight:900;font-size:44px;color:var(--ink);line-height:1;white-space:nowrap}
.center{left:0;width:1200px;text-align:center}
.welcome-text{left:616px;top:783px;width:370px;font-size:11.5px;line-height:15.7px;color:var(--text)}
.welcome-text p+p{margin-top:16px}
.services{left:0;top:1226px;width:1200px;height:587px;background:var(--mint-soft)}
.card{position:absolute;width:249px;border-radius:26px;background:var(--white);box-shadow:0 10px 30px rgba(60,140,80,.08);text-align:center}
.service{top:1411px;height:330px}
.service .icon{width:100px;height:92px;margin:50px auto 0;border-radius:16px}
.service h3{margin-top:26px;font-family:"Nunito",sans-serif;font-weight:700;font-size:22px;color:var(--ink)}
.service p{margin:14px auto 0;width:190px;font-size:12px;line-height:17px;color:var(--text)}
.product{top:2025px;height:328px}
.product .photo{width:170px;height:150px;margin:22px auto 0;border-radius:10px}
.product h4{margin-top:28px;font-family:"Arimo",sans-serif;font-weight:700;font-size:12px;color:#222}
.stars{margin-top:4px;color:#0e7a3e;font-size:12px;letter-spacing:1px}
.price{margin-top:3px;font-family:"Arimo",sans-serif;font-size:11px;font-weight:700;color:#222}
.price s{color:#999;font-weight:400;margin-right:3px}
.cart-btn{display:inline-flex;align-items:center;gap:5px;margin-top:9px;height:24px;padding:0 12px;border:1px solid var(--green);border-radius:12px;font-family:"Arimo",sans-serif;font-size:6.5px;font-weight:700;color:var(--green);white-space:nowrap}
.footer{left:0;top:2557px;width:1200px;height:211px;background:var(--footer);color:var(--white);font-family:"Arimo",sans-serif}
.footer .brand{position:absolute;left:193px;top:50px;font-size:22px;color:var(--white)}
.footer .brand-dot{width:36px;height:36px}
.footer-links{position:absolute;left:394px;top:48px;font-size:9.5px;line-height:17px;white-space:nowrap}
.footer-contact{position:absolute;left:521px;top:48px;font-size:9.5px;line-height:17px;white-space:nowrap}
.news-title{position:absolute;left:757px;top:49px;font-weight:700;font-size:15px;white-space:nowrap}
.news-field{position:absolute;left:759px;top:74px;width:244px;height:24px;border-bottom:1px solid #ccc;font-size:9px;padding-top:8px}
.news-btn{position:absolute;left:932px;top:74px;width:71px;height:24px;background:var(--green-bright);font-size:9px;font-weight:700;display:flex;align-items:center;justify-content:center}
.footer-rule{position:absolute;left:193px;top:163px;width:810px;height:1px;background:#4c4c4c}
.footer-bottom{position:absolute;top:182px;font-size:8.5px;white-space:nowrap}
</style>
</head>
<body>
<div class="page">

  <header class="nav">
    <div class="brand"><span class="brand-dot"></span>Lunavetta</div>
    <nav>
      <span class="nav-link" style="left:421px">ABOUT US</span>
      <span class="nav-link" style="left:493px">ABOUT THE LABORATORY</span>
      <span class="nav-link" style="left:638px">ABOUT CBDP</span>
      <span class="nav-link" style="left:722px">ABOUT THCP</span>
      <span class="nav-link" style="left:805px">SHOP</span>
      <span class="nav-link" style="left:849px">CONTACT US</span>
    </nav>
    <div class="nav-icons">
      <svg width="20" height="18" viewBox="0 0 20 18" fill="none" stroke="#12a150" stroke-width="1.8"><path d="M1 2h3l2.5 10h10l2-7H5.5"/><circle cx="8" cy="15.5" r="1.3"/><circle cx="15" cy="15.5" r="1.3"/></svg>
    </div>
    <svg class="nav-search" width="18" height="18" viewBox="0 0 18 18" fill="none" stroke="#444" stroke-width="2.4"><circle cx="7.5" cy="7.5" r="5.5"/><path d="M11.5 11.5l5 5"/></svg>
  </header>

  <svg class="abs" style="left:0;top:54px" width="1200" height="500" viewBox="0 0 1200 500">
    <path d="M720 0H1200V230C1130 260 1010 240 960 110C930 40 820 70 760 40C730 25 720 10 720 0Z" fill="var(--mint)"/>
    <path d="M820 110C900 60 960 150 1040 180C1110 200 1160 190 1200 170V410C1120 400 1040 440 950 475C880 500 820 460 800 400C770 320 740 170 820 110Z" fill="url(#heroGreen)"/>
    <defs><linearGradient id="heroGreen" x1="0" x2="1"><stop offset="0" stop-color="#0ea04f"/><stop offset="1" stop-color="#07e36e"/></linearGradient></defs>
  </svg>
  <h1 class="abs hero-title">Lunavetta</h1>
  <div class="abs hero-sub">The Next Revolution in Cannabinoids</div>
  <div class="abs hero-text">Lunavetta is the first lab to be able to make the minor cannabinoids TCHP and CBDP in bulk batches.</div>
  <div class="btn" style="left:196px;top:340px">DISCOVER MORE <span>›</span></div>
  <div class="art" role="img" aria-label="White CBD oil dropper bottle with green cap among hemp leaves" style="left:520px;top:158px;width:440px;height:370px;background:radial-gradient(ellipse at 50% 50%,rgba(240,238,230,.95) 0 28%,rgba(60,130,60,.55) 45%,rgba(60,130,60,0) 70%)"></div>

  <svg class="abs" style="left:0;top:612px" width="300" height="535" viewBox="0 0 300 535">
    <path d="M0 5C90-10 190 20 230 100C270 190 260 290 190 350C120 410 60 500 0 532Z" fill="var(--green)"/>
  </svg>
  <div class="art" role="img" aria-label="CBD oil dropper bottle surrounded by hemp leaves" style="left:107px;top:612px;width:420px;height:452px;background:radial-gradient(ellipse at 45% 55%,rgba(242,240,232,1) 0 26%,rgba(55,120,55,.6) 44%,rgba(55,120,55,0) 70%)"></div>
  <div class="abs eyebrow" style="left:616px;top:697px">WELCOME TO</div>
  <h2 class="abs heading" style="left:613px;top:722px">Lunavetta</h2>
  <div class="abs welcome-text">
    <p>Lunavetta is the first lab to be able to make the minor cannabinoids TCHP and CBDP in bulk batches. These canniboids were are 2 of the 150 cannabinoids found in the hemp plant and 2 of the ones found in the smallest amounts.</p>
    <p>Although most cannabis strains contain very small amounts of THCP and CBDP, the isolation of these phytocannabinoids have the potential to change the way we think about cannabinoids altogether.</p>
  </div>
  <div class="btn" style="left:616px;top:932px">DISCOVER MORE <span>›</span></div>

  <section class="abs services"></section>
  <div class="abs eyebrow center" style="top:1294px">WHAT WE DO</div>
  <h2 class="abs heading center" style="top:1320px">Our Services</h2>
  <div class="card service" style="left:193px">
    <div class="icon" role="img" aria-label="Cannabis plant illustration" style="background:linear-gradient(180deg,#cfe89a,#8bbf3c)"></div>
    <h3>Cannabis Farm</h3>
    <p>We have been producing cannabinoids for many years and we are undeniably proud of the quality of our products.</p>
  </div>
  <div class="card service" style="left:475px">
    <div class="icon" role="img" aria-label="Laboratory flask with cannabis leaf illustration" style="background:linear-gradient(135deg,#f6c79a,#b9dc6a)"></div>
    <h3>CBDP</h3>
    <p>We have been producing cannabinoids for many years and we are undeniably proud of the quality of our products.</p>
  </div>
  <div class="card service" style="left:756px">
    <div class="icon" role="img" aria-label="Storefront with cannabis plants illustration" style="background:linear-gradient(180deg,#9fd36a,#b98a5a)"></div>
    <h3>TCHP</h3>
    <p>We have been producing cannabinoids for many years and we are undeniably proud of the quality of our products.</p>
  </div>

  <svg class="abs" style="left:0;top:2115px" width="440" height="442" viewBox="0 0 440 442">
    <path d="M0 70C60 40 140 20 200 0V240C230 270 300 250 330 250C380 260 420 330 418 442H0Z" fill="var(--mint)"/>
    <path d="M0 70C60 40 140 20 200 0V240H406C400 300 360 330 300 320C240 310 180 230 100 200C60 185 25 200 0 210Z" fill="url(#shopGreen)"/>
    <defs><linearGradient id="shopGreen" x1="0" x2="1"><stop offset="0" stop-color="#0ea04f"/><stop offset="1" stop-color="#07e36e"/></linearGradient></defs>
  </svg>
  <div class="abs eyebrow center" style="top:1890px">OUR BESTSELLERS</div>
  <h2 class="abs heading center" style="top:1916px">Online Shop</h2>
  <div class="card product" style="left:193px">
    <div class="photo" role="img" aria-label="Green CBD tincture bottles with box" style="background:linear-gradient(135deg,#eef3e6,#7ea74a 60%,#2e3b2a)"></div>
    <h4>CBD Tabs</h4><div class="stars">★★★★★</div>
    <div class="price"><s>$24.33</s>$13.25</div>
    <div class="cart-btn"><svg width="8" height="7" viewBox="0 0 20 18" fill="none" stroke="#12a150" stroke-width="2.5"><path d="M1 2h3l2.5 10h10l2-7H5.5"/></svg>ADD TO CART</div>
  </div>
  <div class="card product" style="left:475px">
    <div class="photo" role="img" aria-label="Orange CBD tincture bottles with box" style="background:linear-gradient(135deg,#f6efe6,#e08a26 60%,#3a2a1a)"></div>
    <h4>CBD Tabs</h4><div class="stars">★★★★★</div>
    <div class="price"><s>$24.33</s>$13.25</div>
    <div class="cart-btn"><svg width="8" height="7" viewBox="0 0 20 18" fill="none" stroke="#12a150" stroke-width="2.5"><path d="M1 2h3l2.5 10h10l2-7H5.5"/></svg>ADD TO CART</div>
  </div>
  <div class="card product" style="left:756px">
    <div class="photo" role="img" aria-label="Stack of pastel chocolate bar packages" style="background:linear-gradient(135deg,#e9c9cf,#e8dcb8 45%,#a9c9b0 65%,#5a3a2e)"></div>
    <h4>CBD Tabs</h4><div class="stars">★★★★★</div>
    <div class="price"><s>$24.33</s>$13.25</div>
    <div class="cart-btn"><svg width="8" height="7" viewBox="0 0 20 18" fill="none" stroke="#12a150" stroke-width="2.5"><path d="M1 2h3l2.5 10h10l2-7H5.5"/></svg>ADD TO CART</div>
  </div>
  <div class="btn" style="left:529px;top:2427px">DISCOVER MORE <span>›</span></div>

  <footer class="abs footer">
    <div class="brand"><span class="brand-dot"></span>Lunavetta</div>
    <div class="footer-links">About Us<br>About the Laboratory<br>About CBDP<br>About THCP<br>Shop<br>Contact Us</div>
    <div class="footer-contact">48 Marlow Creek Rd, Fernvale, TN 37000<br>Call Us: 800.555.0142<br>hello@lunavetta.com</div>
    <div class="news-title">Newsletter Sign Up</div>
    <div class="news-field">Email Address</div>
    <div class="news-btn">Subscribe</div>
    <div class="footer-rule"></div>
    <div class="footer-bottom" style="left:196px">© Lunavetta 2021 I. All Rights Reserved.</div>
    <div class="footer-bottom" style="left:849px">Terms Of Use</div>
    <div class="footer-bottom" style="left:925px">Privacy Policy</div>
  </footer>
</div>
</body>
</html>
```